Email Banner: Pale Harbor

Need an email banner for https://pale-harbor.example/ much the same design for the attatched just using the logo and brand as the guidance.

Tagline should be "Essential Whitepapers for Business Professionals" or "Whitepapers featured from the most reputable companies in the industry"

It will be going on an email that looks like this:

https://mailvista.example/emails/preview/fullscreen/a17d3b2e-8c4f-4e1a-9b6d-f24e8a1c5d90

So dont make it to thick and clunky.

Target Market(s)

IT Proffesioanls

Industry/Entity Type

Information Technology

Logo Text

Essential Whitepapers for Business Professionals

Logo styles of interest
Abstract Logo
Font styles to use
Sans Serif

Colors
0054AA
0677BA
7BADD7
CADEEF
E8F1F8

Requirements
Must have
• Logo and colour scheme from the weblink provided: https://pale-harbor.example/

```html
<!DOCTYPE html>
<html lang="en">
<head>
<meta charset="UTF-8">
<title>Pale Harbor – Email Banner</title>
<link href="https://fonts.googleapis.com/css2?family=Figtree:wght@400;600;700;800&display=swap" rel="stylesheet">
<style>
  :root {
    --canvas: #ffffff;
    --ink: #0b2545;
    --frame: #7badd7;
    --brand-blue: #0054aa;
    --ocean-blue: #0677ba;
    --sky-blue: #7badd7;
    --pale-blue: #cadeef;
    --mist-blue: #e8f1f8;
    --light-text: #ffffff;
  }
  * { box-sizing: border-box; margin: 0; padding: 0; }
  html, body {
    width: 1200px;
    height: 1200px;
    overflow: hidden;
    background: var(--canvas);
    font-family: "Figtree", Arial, sans-serif;
  }
  .stage {
    position: relative;
    width: 1200px;
    height: 1200px;
  }
  .email-banner {
    position: absolute;
    left: 177px;
    top: 532px;
    width: 845px;
    height: 135px;
    border: 1px solid var(--frame);
    overflow: hidden;
    background: var(--canvas);
  }
  .banner-shapes {
    position: absolute;
    inset: 0;
    width: 100%;
    height: 100%;
  }
  .accent-stripe { fill: var(--ocean-blue); }
  .cta-tab { fill: var(--brand-blue); }
  .brand {
    position: absolute;
    left: 34px;
    top: 45px;
    display: flex;
    align-items: center;
    gap: 14px;
  }
  .brand-dot {
    width: 42px;
    height: 42px;
    border-radius: 50%;
    background: var(--brand-blue);
  }
  .brand-name {
    font-size: 34px;
    font-weight: 700;
    color: var(--ink);
    letter-spacing: -0.2px;
    line-height: 1;
  }
  .tagline {
    position: absolute;
    left: 402px;
    top: 38px;
    color: var(--light-text);
    font-size: 23px;
    font-weight: 400;
    line-height: 31px;
  }
  .tagline strong { font-weight: 700; }
  .cta {
    position: absolute;
    right: 20px;
    top: 0;
    height: 41px;
    display: flex;
    align-items: center;
    color: var(--light-text);
    font-size: 16px;
    font-weight: 800;
    letter-spacing: 0.3px;
    text-decoration: none;
  }
</style>
</head>
<body>
  <main class="stage">
    <section class="email-banner" aria-label="Pale Harbor email banner">
      <svg class="banner-shapes" viewBox="0 0 845 135" preserveAspectRatio="none" aria-hidden="true">
        <defs>
          <linearGradient id="panelFade" x1="0" y1="0" x2="1" y2="0">
            <stop offset="0" style="stop-color:var(--brand-blue)"/>
            <stop offset="0.5" style="stop-color:var(--ocean-blue)"/>
            <stop offset="0.85" style="stop-color:var(--sky-blue)"/>
            <stop offset="1" style="stop-color:var(--mist-blue)"/>
          </linearGradient>
        </defs>
        <polygon class="accent-stripe" points="281,0 310,0 384,135 356,135"/>
        <polygon class="message-panel" points="305,0 845,0 845,135 380,135" fill="url(#panelFade)"/>
        <polygon class="cta-tab" points="693,0 845,0 845,41 714,41"/>
      </svg>

      <div class="brand">
        <span class="brand-dot"></span>
        <span class="brand-name">Pale Harbor</span>
      </div>

      <p class="tagline">Essential Whitepapers<br>for <strong>Business Professionals</strong></p>

      <a class="cta" href="https://pale-harbor.example/">CLICK HERE</a>
    </section>
  </main>
</body>
</html>
```